2018 Vision Board Workshop

I need to promote this workshop on both an 8.5x11 sheet and a 5x7 card. I do have a logo that needs to be present. I'd like to stay true to my branded colors. The flyer needs to project the excitement of a new year and the possibilities of what a person can create, produce, explore in their lives by putting it all on a vision board. Creating the vision of what you want will inspire you to achieve your goals and dreams. Looking at your vision board each day will propel you into taking action as you chart your course to achieve what you truly want.
The flyer needs to have the following information:
The workshop date and time - Sat., Jan. 13, 2018, 10:30-1:30
The location is - Atrium 47B, 2864 Birchwood Vale Rd, Colorado Springs, Co 80417
in the FORGE Room
My name and contact information - Mara Vollbeck
Text and voice 303-417-6652
Email - mara@brightwell-daily-craft.com
Website - brightwell-daily-craft.com
The fee is $45. All materials are provided.

My company is called Brightwell Daily Craft. I am a Life Coach, author, speaker and workshop leader.\ I wrote this program, Brightwell Daily Craft to teach concepts and supporting skills for living with more happiness, satisfaction and fulfillment. Thanks for reading this!! Mara

Target Market(s)

Primarily women, educated, motivated, proactive in their own lives and well being

Font styles to use
Other font styles liked:
• I have been using Century Gothic. I'm open to new ideas.

Requirements
Must have
• The Brightwell Daily Craft logo
• The flyer needs to have the following information:
• The workshop date and time - Sat., Jan. 13, 2018, 10:30-1:30
• The location is - Atrium 47B, 2864 Birchwood Vale Rd, Colorado Springs, Co 80417
• in the FORGE Room
• My name and contact information - Mara Vollbeck
• Text and voice 303-417-6652
• Email - mara@brightwell-daily-craft.com
• Website - brightwell-daily-craft.com
• The fee is $45. All materials are provided.
Nice to have
• The Brightwell Daily Craft branded colors in the design
• Images of vision boards

```html
<!DOCTYPE html>
<html lang="en">
<head>
<meta charset="utf-8">
<title>Vision Board Workshop Flyer</title>
<link href="https://fonts.googleapis.com/css2?family=Poppins:wght@300;400;500;600&family=Questrial&family=PT+Sans:wght@400;700&display=swap" rel="stylesheet">
<style>
  :root {
    --brand-blue: #2f86c8;
    --brand-blue-light: #3ba8e0;
    --brand-blue-deep: #2a6fb8;
    --brand-green: #8cc63f;
    --brand-green-bright: #8ed61c;
    --text-gray: #7a7a7a;
    --paper: #ffffff;
    --page-bg: #e9eaec;
    --board-top: #f4f8fd;
    --board-bottom: #e3ecf7;
    --pin: #4a4340;
  }
  * { box-sizing: border-box; margin: 0; padding: 0; }
  html, body { width: 1200px; height: 1200px; overflow: hidden; }
  body { background: var(--page-bg); position: relative; font-family: "Questrial", sans-serif; }

  .flyer {
    position: absolute; left: 150px; top: 18px;
    width: 900px; height: 1164px;
    background: var(--paper);
    overflow: hidden;
    box-shadow: 0 4px 14px rgba(0,0,0,.18);
  }
  .band { position: absolute; left: 0; width: 900px; display: block; }
  .band--top { top: 0; height: 100px; }
  .band--bottom { top: 960px; height: 204px; }

  .board {
    position: absolute; left: 35px; top: 93px; width: 840px; height: 517px;
    background: linear-gradient(160deg, var(--board-top), var(--board-bottom));
    border-radius: 3px;
    box-shadow: 0 2px 6px rgba(0,0,0,.25);
    overflow: hidden;
  }
  .pin { position: absolute; width: 12px; height: 12px; border-radius: 50%; background: var(--pin); box-shadow: 0 1px 2px rgba(0,0,0,.4); }

  .brand-name {
    position: absolute; left: 330px; top: 118px; width: 480px; text-align: center;
    font-family: "Questrial", sans-serif; font-size: 42px; color: var(--brand-green-bright);
    white-space: nowrap;
  }

  .photo { position: absolute; box-shadow: 0 3px 8px rgba(0,0,0,.3); }
  .photo--woman { left: 30px; top: 25px; width: 285px; height: 300px; transform: rotate(-8deg); background: linear-gradient(135deg, #7d8a5a, #c9a587 55%, #8f7a60); }
  .photo--finance { left: 70px; top: 322px; width: 262px; height: 172px; transform: rotate(4deg); background: linear-gradient(135deg, #eeeae2, #d8d2c4 60%, #c9a66f); }
  .photo--shop { left: 312px; top: 208px; width: 215px; height: 232px; transform: rotate(-6deg); background: linear-gradient(150deg, #b9c4ae, #8fa886 55%, #6c6f5e); }
  .photo--family { left: 548px; top: 200px; width: 280px; height: 235px; transform: rotate(5deg); background: linear-gradient(180deg, #cfe6f3, #7fc3de 55%, #a99b88); }
  .photo--travel { left: 516px; top: 378px; width: 176px; height: 128px; transform: rotate(-4deg); background: linear-gradient(160deg, #9fd2ee, #3a94cf 60%, #1f6fae); }

  .headline { position: absolute; left: 99px; top: 652px; width: 320px; }
  .headline__line {
    display: block; font-family: "Poppins", sans-serif; font-weight: 300; line-height: 1;
    white-space: nowrap;
  }
  .headline__line--vision, .headline__line--board { font-size: 68px; color: var(--brand-green); height: 61px; }
  .headline__line--vision { letter-spacing: 19.5px; }
  .headline__line--board { letter-spacing: 21.5px; }
  .headline__line--workshop { font-size: 55px; font-weight: 400; color: var(--brand-blue-deep); margin-top: 2px; }

  .pitch {
    position: absolute; left: 80px; top: 836px; width: 323px; text-align: right;
    font-family: "Questrial", sans-serif; font-size: 15px; line-height: 29.5px; letter-spacing: 3px;
    color: var(--text-gray); text-transform: uppercase;
  }
  .pitch strong { font-family: "Poppins", sans-serif; font-weight: 500; color: #666; font-size: 14.5px; }

  .divider { position: absolute; left: 446px; top: 644px; width: 1.5px; height: 342px; background: var(--brand-blue-light); }

  .details { position: absolute; left: 475px; top: 682px; width: 400px; color: var(--brand-blue-light); }
  .details__day { font-family: "Questrial", sans-serif; font-size: 31px; letter-spacing: 3px; line-height: 38px; }
  .details__date { font-family: "Poppins", sans-serif; font-weight: 600; font-size: 30px; letter-spacing: 2px; line-height: 38px; color: var(--brand-blue); }
  .details__time { font-family: "Questrial", sans-serif; font-size: 31px; letter-spacing: 3px; line-height: 38px; }
  .details__venue {
    margin-top: 15px; font-family: "Questrial", sans-serif; font-size: 13.5px; line-height: 20.5px;
    letter-spacing: 2.6px; color: var(--text-gray); text-transform: uppercase;
  }
  .details__fee { margin-top: 26px; font-family: "Questrial", sans-serif; font-size: 24px; letter-spacing: 1.5px; color: var(--brand-green); text-transform: uppercase; }
  .details__materials { margin-top: 4px; font-family: "Questrial", sans-serif; font-size: 17px; letter-spacing: 1.5px; color: var(--brand-green); text-transform: uppercase; }

  .contact { position: absolute; left: 0; top: 1066px; width: 900px; color: #fff; font-family: "PT Sans", sans-serif; }
  .contact__line { position: absolute; left: 107px; top: 0; font-size: 29px; white-space: nowrap; }
  .contact__line strong { font-weight: 700; }
  .contact__item { position: absolute; top: 50px; display: flex; align-items: center; gap: 14px; font-size: 23px; white-space: nowrap; }
  .contact__item--email { left: 43px; }
  .contact__item--web { left: 504px; }
  .contact__icon { width: 36px; height: 36px; border-radius: 9px; background: #fff; display: flex; align-items: center; justify-content: center; flex: none; }
</style>
</head>
<body>
  <main class="flyer">
    <svg class="band band--top" viewBox="0 0 900 100" preserveAspectRatio="none" aria-hidden="true">
      <defs>
        <linearGradient id="topBlue" x1="0" y1="0" x2="1" y2="0">
          <stop offset="0" stop-color="#2f7fc4"/><stop offset=".5" stop-color="#3aa9e0"/><stop offset="1" stop-color="#2f7fc4"/>
        </linearGradient>
      </defs>
      <path d="M0 0 H900 V62 Q450 -10 0 76 Z" fill="url(#topBlue)"/>
      <path d="M0 76 Q450 -10 900 62 V74 Q450 10 0 90 Z" fill="var(--brand-green)"/>
    </svg>

    <section class="board">
      <div class="photo photo--woman" role="img" aria-label="Photo of a smiling woman outdoors wearing earphones"></div>
      <div class="photo photo--finance" role="img" aria-label="Photo of hands counting money beside a calculator"></div>
      <div class="photo photo--shop" role="img" aria-label="Photo of a shop owner hanging an open sign"></div>
      <div class="photo photo--family" role="img" aria-label="Photo of a family walking on a pier by the sea"></div>
      <div class="photo photo--travel" role="img" aria-label="Photo of an airplane flying through blue sky and clouds"></div>
      <div class="brand-name">Brightwell Daily Craft</div>
    </section>
    <span class="pin" style="left:113px;top:83px"></span>
    <span class="pin" style="left:796px;top:83px"></span>
    <span class="pin" style="left:112px;top:605px"></span>
    <span class="pin" style="left:792px;top:607px"></span>

    <h1 class="headline">
      <span class="headline__line headline__line--vision">VISION</span>
      <span class="headline__line headline__line--board">BOARD</span>
      <span class="headline__line headline__line--workshop">WORKSHOP</span>
    </h1>
    <p class="pitch">Feel the excitement of this<br>new year as you explore<br>what you want to create<br>and accomplish by putting<br>it all on a <strong>vision board</strong>!</p>

    <div class="divider"></div>

    <section class="details">
      <p class="details__day">SATURDAY</p>
      <p class="details__date">JANUARY 13, 2018</p>
      <p class="details__time">10:30 A.M - 1:30 P.M.</p>
      <p class="details__venue">Atrium 47B, 2864 Birchwood Vale Rd,<br>Colorado Springs, CO 80417<br>(at FORGE Room)</p>
      <p class="details__fee">Workshop fee $45</p>
      <p class="details__materials">All materials are provided</p>
    </section>

    <svg class="band band--bottom" viewBox="0 0 900 204" preserveAspectRatio="none" aria-hidden="true">
      <defs>
        <linearGradient id="bottomBlue" x1="0" y1="0" x2="1" y2="0">
          <stop offset="0" stop-color="#2d74bd"/><stop offset=".5" stop-color="#3a9fdb"/><stop offset="1" stop-color="#2d74bd"/>
        </linearGradient>
      </defs>
      <path d="M0 24 Q440 160 900 12 V204 H0 Z" fill="url(#bottomBlue)"/>
      <path d="M0 8 Q440 148 900 0 V12 Q440 160 0 24 Z" fill="var(--brand-green)"/>
    </svg>

    <section class="contact">
      <p class="contact__line"><strong>MARA VOLLBECK</strong> TEXT AND VOICE 303-417-6652</p>
      <p class="contact__item contact__item--email">
        <span class="contact__icon">
          <svg width="24" height="18" viewBox="0 0 24 18" aria-hidden="true"><rect x="1" y="1" width="22" height="16" rx="1.5" fill="none" stroke="#2f86c8" stroke-width="2"/><path d="M1 2 L12 11 L23 2 M1 16 L9 9 M23 16 L15 9" fill="none" stroke="#2f86c8" stroke-width="1.6"/></svg>
        </span>
        MARA@BRIGHTWELL-DAILY-CRAFT.COM
      </p>
      <p class="contact__item contact__item--web">
        <span class="contact__icon">
          <svg width="24" height="24" viewBox="0 0 24 24" aria-hidden="true"><g fill="none" stroke="#2f86c8" stroke-width="1.6"><circle cx="12" cy="12" r="10"/><ellipse cx="12" cy="12" rx="4.5" ry="10"/><path d="M2 12 H22 M4 6.5 H20 M4 17.5 H20 M12 2 V22"/></g></svg>
        </span>
        BRIGHTWELL-DAILY-CRAFT.COM
      </p>
    </section>
  </main>
</body>
</html>
```